Business card for new business.
Red and black corporate colors.
Card can have an Indsutrial feel to it. Feel free to add Rust, Bolted steel, or graphics as you see fit. We provide highly specialized services to the below mentioned industries.
Keep information out of corners so that if I want I can choose rounded corners.
Information
- front. name - title - phone - email
- Rear
Refining - Rail - Infrastructure - Mining - Energy
Alderby - Westmoor - Port Haverill - Kestrel Bay - Dunmarrow

```html
<!DOCTYPE html>
<html lang="en">
<head>
<meta charset="UTF-8">
<title>Girdwell Business Card</title>
<link href="https://fonts.googleapis.com/css2?family=Open+Sans:wght@400;600;700;800&display=swap" rel="stylesheet">
<style>
  :root {
    --backdrop: #d9d6d2;
    --card: #151515;
    --card-edge: #1f1f1f;
    --red: #e2202a;
    --grey: #8a8a8a;
    --text: #e8e8e8;
    --muted: #b9b9b9;
  }
  * { margin: 0; padding: 0; box-sizing: border-box; }
  html, body {
    width: 1200px; height: 864px; overflow: hidden;
    background: var(--backdrop);
    font-family: "Open Sans", Arial, sans-serif;
  }
  .stage { position: relative; width: 1200px; height: 864px; }
  .card {
    position: absolute; left: 320px; width: 560px; height: 320px;
    background: linear-gradient(160deg, var(--card-edge), var(--card) 60%);
    box-shadow: 0 10px 28px rgba(0,0,0,.28);
  }
  .card-rear { top: 80px; }
  .card-front { top: 464px; }

  .wordmark {
    display: flex; align-items: center; gap: 12px;
    font-weight: 800; color: var(--grey); letter-spacing: 1px;
  }
  .wordmark-square { width: 14px; height: 14px; background: var(--red); flex: none; }

  .card-rear .wordmark {
    position: absolute; top: 100px; left: 0; right: 0;
    justify-content: center; font-size: 50px; line-height: 1;
  }
  .sectors {
    position: absolute; top: 182px; left: 0; right: 0;
    text-align: center; color: var(--muted); font-size: 15px; line-height: 1.55;
  }
  .sectors .dot { color: var(--red); margin: 0 5px; }

  .card-front .wordmark {
    position: absolute; top: 132px; left: 46px; font-size: 40px; line-height: 1;
  }
  .divider {
    position: absolute; left: 318px; top: 86px; width: 1px; height: 148px;
    background: linear-gradient(transparent, #6a6a6a 30%, #6a6a6a 70%, transparent);
  }
  .contact { position: absolute; left: 340px; top: 106px; }
  .contact-name { color: var(--red); font-weight: 700; font-size: 19px; line-height: 1.2; }
  .contact-title { color: var(--text); font-size: 15px; margin-bottom: 10px; }
  .contact-line {
    display: flex; align-items: center; gap: 8px;
    color: var(--text); font-size: 15px; line-height: 1.6;
  }
  .contact-line svg { width: 12px; height: 12px; flex: none; }
</style>
</head>
<body>
<main class="stage">
  <section class="card card-rear" aria-label="Card back">
    <div class="wordmark"><span class="wordmark-square"></span>GIRDWELL</div>
    <p class="sectors">
      Refining<span class="dot">•</span>Rail<span class="dot">•</span>Infrastructure<span class="dot">•</span>Mining<br>
      Energy<span class="dot">•</span>Alderby<span class="dot">•</span>Westmoor<span class="dot">•</span>Port Haverill<br>
      Kestrel Bay<span class="dot">•</span>Dunmarrow
    </p>
  </section>

  <section class="card card-front" aria-label="Card front">
    <div class="wordmark"><span class="wordmark-square"></span>GIRDWELL</div>
    <div class="divider"></div>
    <div class="contact">
      <p class="contact-name">MARK TOLEN</p>
      <p class="contact-title">PRESIDENT</p>
      <p class="contact-line">
        <svg viewBox="0 0 12 12"><path fill="#e2202a" d="M2 1h2.5l1 2.5-1.3 1a6 6 0 0 0 3.3 3.3l1-1.3L11 7.5V10a1 1 0 0 1-1 1A9 9 0 0 1 1 2a1 1 0 0 1 1-1z"/></svg>
        555 0142 7781
      </p>
      <p class="contact-line">
        <svg viewBox="0 0 12 12"><rect x="0.5" y="2" width="11" height="8" fill="#e2202a"/><path d="M0.5 2.3 6 6.5l5.5-4.2" stroke="#151515" fill="none"/></svg>
        mark@girdwell.com
      </p>
      <p class="contact-line">
        <svg viewBox="0 0 12 12"><circle cx="6" cy="6" r="5.5" fill="#e2202a"/><path d="M0.5 6h11M6 0.5c-2.5 3-2.5 8 0 11M6 0.5c2.5 3 2.5 8 0 11" stroke="#151515" stroke-width=".8" fill="none"/></svg>
        www.girdwell.com
      </p>
    </div>
  </section>
</main>
</body>
</html>
```